Bright Harbor Concierge

I need a website developed for our travel concierge service. I'm looking to be able to collect information and have the information collected directed to a inbox. I would also like to me able to manage the updates to the website myself. I also would like a mobile version of the website to be included. Our services include assistance with Bachelor Parties, Bachelorette Parties and Medical Tourism. We provide custom packages that include Airport Transportation, Lodging, Bilingual guides and any other special needs identified by our clients.
Industry/Entity Type
Travel
Coding
Coded - Design and coding required
Number of Pages Required
4 page
Look and feel

```html
<!DOCTYPE html>
<html lang="en">
<head>
<meta charset="utf-8">
<title>Bright Harbor Concierge</title>
<link rel="stylesheet" href="https://fonts.googleapis.com/css2?family=Lora:wght@600;700&family=Nunito+Sans:wght@400;600;800&display=swap">
<style>
:root{
  --gold:#d98f21;
  --ink:#0b0b0b;
  --black:#000;
  --white:#fff;
}
*{box-sizing:border-box;margin:0;padding:0}
html,body{width:1200px;height:3534px;overflow:hidden}
body{position:relative;background:var(--ink);color:var(--white);font-family:"Nunito Sans",Arial,sans-serif}
.abs{position:absolute}
.serif{font-family:"Lora",Georgia,serif}
.gold{color:var(--gold)}
.btn{position:absolute;display:flex;align-items:center;justify-content:center;background:var(--gold);color:var(--black);font-weight:800;font-size:15px;letter-spacing:.3px;border-radius:26px;height:50px;text-transform:uppercase}

/* header */
.header{left:0;top:0;width:1200px;height:103px;background:var(--black)}
.topbar{left:507px;top:0;width:693px;height:37px;background:var(--gold);border-bottom-left-radius:34px;display:flex;align-items:center;padding-left:52px;font-size:14px;color:var(--black);font-weight:600;z-index:2}
.topbar b{font-weight:800}
.topbar .sep{margin:0 18px;font-weight:800}
.topbar .social{margin-left:auto;margin-right:112px;display:flex;gap:9px}
.topbar .social span{width:11px;height:11px;border-radius:50%;border:2px solid var(--black)}
.brand-badge{left:74px;top:-22px;width:186px;height:186px;border-radius:50%;background:var(--black);display:flex;align-items:center;justify-content:center;text-align:center;padding-top:30px;z-index:3}
.brand-badge span{font-family:"Lora",Georgia,serif;font-weight:600;color:var(--gold);font-size:20px;line-height:1.15}
.nav{right:111px;top:63px;display:flex;gap:27px;font-size:14px;font-weight:800;z-index:3}
.nav .on{color:var(--gold)}

/* hero */
.hero-photo{left:0;top:103px;width:1200px;height:680px;background:
  radial-gradient(circle at 12% 35%,rgba(255,190,100,.35) 0,rgba(255,190,100,0) 9%),
  radial-gradient(circle at 88% 25%,rgba(255,200,110,.4) 0,rgba(255,200,110,0) 10%),
  radial-gradient(ellipse at 50% 62%,#8a5a34 0%,rgba(90,60,36,.8) 28%,rgba(0,0,0,0) 60%),
  linear-gradient(180deg,#2a3038 0%,#3a2e26 40%,#1a120c 100%)}
.hero-curve{left:0;top:600px;width:1200px;height:200px}
.hero-title{left:0;top:210px;width:1200px;text-align:center;font-size:36px;font-weight:700;letter-spacing:.5px}
.hero-sub{left:315px;top:266px;width:570px;text-align:center;font-size:18px;font-weight:800;line-height:28px}

.heading{left:0;width:1200px;text-align:center;font-size:36px;font-weight:700;text-transform:uppercase}

/* services */
.svc{width:310px;height:310px;border-radius:50%;top:962px;overflow:hidden}
.svc-ring{position:absolute;inset:0;border-radius:50%;border:4px solid transparent;border-bottom-color:var(--gold);border-left-color:var(--gold);transform:rotate(-45deg)}
.label{font-size:17px;font-weight:800;text-align:center;text-transform:uppercase;line-height:26px}

/* about */
.about-photo{left:0;top:1423px;width:598px;height:428px;border-radius:0 50% 50% 0/0 50% 50% 0;background:
  radial-gradient(circle at 20% 30%,rgba(255,210,140,.35) 0,rgba(255,210,140,0) 12%),
  radial-gradient(circle at 70% 28%,rgba(255,210,140,.3) 0,rgba(255,210,140,0) 12%),
  radial-gradient(ellipse at 45% 70%,#8a4a2c 0%,rgba(90,50,30,.6) 35%,rgba(0,0,0,0) 65%),
  linear-gradient(180deg,#1c2430,#2a2018 60%,#140e0a);border:4px solid var(--gold);border-left:none}
.about-title{left:651px;top:1470px;font-size:36px;font-weight:700}
.about-text{left:651px;top:1544px;width:438px;font-size:14.5px;line-height:26px;text-align:justify}

/* packages */
.pkg{top:2029px;width:309px;height:203px;border:4px solid var(--gold);border-radius:6px}

/* events */
.event-img{border-radius:6px}
.date{display:flex;align-items:center;gap:14px;font-size:15px}
.date i{width:16px;height:14px;border:2px solid var(--gold);border-top-width:4px;border-radius:2px}
.event-text{font-size:17px;font-weight:800;line-height:27px}

/* footer */
.foot-brand{left:0;top:3240px;width:1200px;text-align:center;font-family:"Lora",Georgia,serif;font-weight:600;color:var(--gold);font-size:28px;line-height:1.1}
.foot-nav{left:0;top:3334px;width:1200px;display:flex;justify-content:center;gap:32px;font-size:17px;font-weight:600}
.foot-contact{left:0;top:3370px;width:1200px;text-align:center;font-size:17px;font-weight:600}
.foot-contact b{color:var(--gold);font-weight:800}
.foot-social{left:0;top:3414px;width:1200px;display:flex;justify-content:center;gap:10px}
.foot-social span{width:36px;height:36px;border-radius:50%;border:2px solid var(--white)}
.foot-social span:first-child{background:var(--gold);border-color:var(--gold)}
.copyright{left:0;top:3480px;width:1200px;height:54px;background:var(--gold);color:var(--black);display:flex;align-items:center;justify-content:center;font-size:13px}
</style>
</head>
<body>

<header>
  <div class="abs header"></div>
  <div class="abs topbar">
    <b>CALL US:</b>&nbsp;(555) 010 2040<span class="sep">|</span><b>EMAIL US:</b>&nbsp;hello@brightharbor.example
    <div class="social"><span></span><span></span><span></span></div>
  </div>
  <div class="abs brand-badge"><span>Bright Harbor<br>Concierge</span></div>
  <nav class="abs nav">
    <span class="on">HOME</span><span>ABOUT US</span><span>OUR SERVICES</span><span>CUSTOM PACKAGES</span><span>LATEST EVENTS</span><span>CONTACT US</span>
  </nav>
</header>

<section class="hero">
  <div class="abs hero-photo" role="img" aria-label="Friends toasting at an evening party under string lights"></div>
  <svg class="abs hero-curve" viewBox="0 0 1200 200" preserveAspectRatio="none" aria-hidden="true">
    <path d="M0 28 Q600 322 1200 28 L1200 200 L0 200 Z" fill="#0b0b0b"/>
    <path d="M0 28 Q600 322 1200 28" fill="none" stroke="#d98f21" stroke-width="6"/>
  </svg>
  <h1 class="abs hero-title serif">WELCOME TO BRIGHT HARBOR CONCIERGE</h1>
  <p class="abs hero-sub">Lorem ipsum dolor sit amet, consectetur adipiscing elit sed eiusmod incididunt ut laborea.</p>
  <span class="btn" style="left:523px;top:346px;width:154px">Get Started</span>
</section>

<section class="services">
  <h2 class="abs heading serif" style="top:866px"><span class="gold">Our</span> Services</h2>
  <div class="abs svc" style="left:110px;background:radial-gradient(circle at 15% 20%,rgba(255,200,120,.45) 0,rgba(255,200,120,0) 14%),radial-gradient(ellipse at 45% 55%,#8a5a3a 0%,#4a3020 45%,#1a120c 100%)" role="img" aria-label="Group of men celebrating a bachelor party"><div class="svc-ring"></div></div>
  <div class="abs svc" style="left:444px;background:radial-gradient(circle at 50% 75%,rgba(255,190,110,.5) 0,rgba(255,190,110,0) 22%),linear-gradient(180deg,#3a332c,#5a4a3a 50%,#1c1612)" role="img" aria-label="Women toasting at a candlelit bachelorette dinner"><div class="svc-ring"></div></div>
  <div class="abs svc" style="left:779px;background:linear-gradient(180deg,#a9b7c4 0%,#6d7a4e 22%,#8a7a5a 45%,#4f86a0 62%,#3a5a6a 100%)" role="img" aria-label="Traveller in a wheelchair by the seaside"><div class="svc-ring"></div></div>
  <div class="abs label" style="left:110px;top:1305px;width:310px">Bachelor Parties</div>
  <div class="abs label" style="left:444px;top:1305px;width:310px">Bachelorette Parties</div>
  <div class="abs label" style="left:779px;top:1305px;width:310px">Medical Tourism</div>
</section>

<section class="about">
  <div class="abs about-photo" role="img" aria-label="Friends dancing with sparklers at a night celebration"></div>
  <h2 class="abs about-title serif">ABOUT <span class="gold">US</span></h2>
  <p class="abs about-text">Lorem ipsum dolor sit amet, consectetur adipiscing elit, sed do eiusmod tempor incididunt ut labore et dolore magna aliq ua. Ut enim ad minim veniam, quis nostrud exercitation ullam co laboris nisi ut aliquip ex ea commodo consequat. Duis aute irure dolor in reprehenderit in voluptate velit esse cillum dolore eu fugiat nulla paquis nostrud riatur.</p>
  <span class="btn" style="left:651px;top:1738px;width:147px">Learn More</span>
</section>

<section class="packages">
  <h2 class="abs heading serif" style="top:1937px"><span class="gold">Custom</span> Packages</h2>
  <div class="abs pkg" style="left:111px;background:radial-gradient(ellipse at 65% 35%,#f3d0a0 0%,#c98a5a 35%,#5a4440 80%),#3a2e2a" role="img" aria-label="Traveller with a suitcase at an airport window"></div>
  <div class="abs pkg" style="left:446px;background:linear-gradient(180deg,#6a4a30 0%,#a07850 22%,#d8d4ce 48%,#b8b2aa 75%,#5a544e 100%)" role="img" aria-label="Bright modern lodging lounge"></div>
  <div class="abs pkg" style="left:780px;background:linear-gradient(180deg,#c8ccd2 0%,#9aa3ad 30%,#a8594a 55%,#4a5d78 80%,#3a4048 100%)" role="img" aria-label="Group of tourists with a local guide and a map"></div>
  <div class="abs label" style="left:111px;top:2252px;width:309px">Airport<br>Transportation</div>
  <div class="abs label" style="left:446px;top:2252px;width:309px">Lodging</div>
  <div class="abs label" style="left:780px;top:2252px;width:309px">Bilingual Guides</div>
  <span class="btn" style="left:494px;top:2341px;width:212px">View More Packages</span>
</section>

<section class="events">
  <h2 class="abs heading serif" style="top:2563px">Latest <span class="gold">Events</span></h2>
  <div class="abs event-img" style="left:111px;top:2662px;width:406px;height:195px;background:radial-gradient(ellipse at 55% 40%,#c48a90 0%,#7a3a50 40%,#2a1420 100%)" role="img" aria-label="Women celebrating under festoon lights"></div>
  <div class="abs date" style="left:111px;top:2881px"><i></i>09 Dec 2021</div>
  <p class="abs event-text" style="left:111px;top:2917px;width:400px">Lorem ipsum dolor sit amet, consectetur adi cing elit, sed do eiusmod tempor incididunt ut labore et dolore magna aliqua.</p>
  <span class="btn" style="left:111px;top:3017px;width:145px">Read More</span>

  <div class="abs event-img" style="left:531px;top:2662px;width:279px;height:194px;background:linear-gradient(180deg,#6a727a 0%,#d8dade 40%,#c8c4c0 70%,#8a6a62 100%)" role="img" aria-label="Couple walking with luggage through a terminal"></div>
  <div class="abs event-img" style="left:531px;top:2874px;width:279px;height:194px;background:radial-gradient(ellipse at 40% 90%,#f0a050 0%,rgba(240,160,80,0) 40%),linear-gradient(180deg,#8aa0c0,#5a6a85 55%,#2a3040)" role="img" aria-label="Friends dancing at a lantern-lit evening gathering"></div>

  <div class="abs date" style="left:842px;top:2665px"><i></i>09 Dec 2021</div>
  <p class="abs event-text" style="left:842px;top:2700px;width:250px">Lorem ipsum dolor sit ame consectetur adipiscing elit sed do eiusa</p>
  <span class="btn" style="left:842px;top:2801px;width:146px">Read More</span>
  <div class="abs date" style="left:842px;top:2877px"><i></i>09 Dec 2021</div>
  <p class="abs event-text" style="left:842px;top:2912px;width:250px">Lorem ipsum dolor sit ame consectetur adipiscing elit sed do eiusa</p>
  <span class="btn" style="left:842px;top:3013px;width:146px">Read More</span>
</section>

<footer>
  <div class="abs foot-brand">Bright Harbor<br>Concierge</div>
  <nav class="abs foot-nav"><span>HOME</span><span>ABOUT US</span><span>OUR SERVICES</span><span>CUSTOM PACKAGES</span><span>LATEST EVENTS</span><span>CONTACT US</span></nav>
  <p class="abs foot-contact"><b>CALL US:</b> (555) 010 2040 &nbsp;&nbsp;|&nbsp;&nbsp; <b>EMAIL US:</b> hello@brightharbor.example</p>
  <div class="abs foot-social"><span></span><span></span><span></span></div>
  <div class="abs copyright">©&nbsp;2021&nbsp;<b>BRIGHT HARBOR CONCIERGE</b>. All Rights Reserved</div>
</footer>

</body>
</html>
```